Business Card Design

Electronic Security
Alarm Systems
CCTV
Electronic Access Control
Security System Integration

Industry/Entity Type

Business

Contact Information for Business Card

Declan Whitfield
PO Box 862
Carrowbrook Qld 4179
Phone 07 38265014
Mob 0428615937

```html
<!DOCTYPE html>
<html lang="en">
<head>
<meta charset="utf-8">
<title>Sentivo Security – Business Card</title>
<link rel="stylesheet" href="https://fonts.googleapis.com/css2?family=Open+Sans:ital,wght@0,400;0,600;0,700;1,400;1,700&display=swap">
<style>
  :root {
    --backdrop: #141414;
    --card: #ffffff;
    --ink: #1f1f1f;
    --muted: #3a3a3a;
    --accent: #2a8fd0;
    --band: #2b2b2b;
    --band-text: #e6e6e6;
    --mark: #2a8fd0;
  }
  * { box-sizing: border-box; margin: 0; padding: 0; }
  html, body {
    width: 1200px; height: 864px; overflow: hidden;
    background: var(--backdrop);
    font-family: "Open Sans", Arial, sans-serif;
  }
  .stage {
    width: 1200px; height: 864px;
    display: flex; align-items: center; justify-content: center; gap: 40px;
  }
  .card {
    position: relative;
    width: 540px; height: 330px;
    background: var(--card);
    overflow: hidden;
    box-shadow: 0 12px 30px rgba(0,0,0,.6);
  }
  .card__band {
    position: absolute; left: 0; right: 0; bottom: 0; height: 52px;
    background: var(--band);
    border-top: 4px solid var(--accent);
    box-shadow: 0 -4px 0 #fff, 0 -6px 0 var(--accent);
  }
  .brand {
    display: flex; align-items: center; gap: 10px;
  }
  .brand__square {
    width: 22px; height: 22px; background: var(--mark);
  }
  .brand__name {
    font-weight: 600; font-size: 30px; color: var(--mark); letter-spacing: .5px;
  }
  /* front */
  .card--front .brand {
    position: absolute; left: 44px; top: 120px;
  }
  .card__divider {
    position: absolute; left: 272px; top: 70px;
    width: 2px; height: 150px;
    background: linear-gradient(to bottom, transparent, #555 30%, #555 70%, transparent);
    transform: rotate(10deg);
  }
  .contact {
    position: absolute; left: 304px; top: 78px;
    color: var(--muted); font-size: 13px; line-height: 1.45;
  }
  .contact__name {
    font-weight: 700; font-size: 19px; color: var(--ink);
    margin-bottom: 12px; margin-left: 24px;
  }
  .contact__address { margin-left: 14px; margin-bottom: 16px; }
  .contact__label { color: var(--accent); font-weight: 700; font-style: italic; }
  /* back */
  .card--back .brand {
    position: absolute; left: 50%; top: 118px; transform: translateX(-50%);
  }
  .services {
    position: absolute; left: 0; right: 0; bottom: 0; height: 48px;
    padding: 0 14px;
    display: flex; align-items: center; justify-content: center;
    color: var(--band-text); font-size: 10px; letter-spacing: 0;
    white-space: nowrap;
  }
</style>
</head>
<body>
<main class="stage">
  <section class="card card--front" aria-label="Card front">
    <div class="brand">
      <span class="brand__square"></span>
      <span class="brand__name">Sentivo</span>
    </div>
    <span class="card__divider"></span>
    <div class="contact">
      <p class="contact__name">Declan Whitfield</p>
      <p class="contact__address">PO Box 862 Carrowbrook<br>Qld 4179</p>
      <p><span class="contact__label">Phone:</span> 07 38265014</p>
      <p><span class="contact__label">Mobile:</span> 0428615937</p>
    </div>
    <div class="card__band"></div>
  </section>

  <section class="card card--back" aria-label="Card back">
    <div class="brand">
      <span class="brand__square"></span>
      <span class="brand__name">Sentivo</span>
    </div>
    <div class="card__band"></div>
    <p class="services">Electronic Security | Alarm Systems | CCTV | Electronic Access Control | Security System Integration</p>
  </section>
</main>
</body>
</html>
```